Bref créative
Home provement Flyer/Door hanger
Kitchen,bathroom,windows
Im looking to make flyer or door hanger for home improvement company. I was thinking front side with kitchen & bathroom.
Back side windows.
Construction
Professional, corporate,
Tallow Ridge Builders, LLC
4817 Copper Fern RD
Suite 812
Larkmoor, VA 00000
Tel: 555 010 4821
www.tallowridgebuilders.example
We offer Financing
Free Estimate
I need the design to be on AI, EPS AND PSD FILE. I need them by each layer so i can edit later if i need to.
This is the company logo.
You may visit www.tallowridgebuilders.example and choose a right picture from the gallery

```html
<!DOCTYPE html>
<html lang="en">
<head>
<meta charset="utf-8">
<title>Tallow Ridge Builders – Flyer and Door Hanger</title>
<link href="https://fonts.googleapis.com/css2?family=Open+Sans:wght@400;600;700;800&display=swap" rel="stylesheet">
<style>
  :root{
    --stage:#2b2d30;
    --paper:#ffffff;
    --ink:#222222;
    --muted:#555555;
    --green:#5cb31f;
    --green-dark:#3d8a12;
    --black:#141414;
    --footer-text:#cfcfcf;
    --photo-warm-a:#b88a5c;
    --photo-warm-b:#5e4632;
    --photo-cool-a:#c9d3da;
    --photo-cool-b:#7d8a92;
  }
  *{box-sizing:border-box;margin:0;padding:0}
  html,body{width:1200px;height:356px;overflow:hidden}
  body{
    background:var(--stage);
    font-family:"Open Sans",Arial,sans-serif;
    color:var(--ink);
    display:flex;align-items:center;justify-content:center;gap:34px;
  }
  .piece{
    background:var(--paper);
    height:316px;
    display:flex;flex-direction:column;
    overflow:hidden;
    position:relative;
  }
  .flyer{width:200px}
  .hanger{width:136px}
  .hanger-top{
    height:62px;flex:none;display:flex;align-items:center;justify-content:center;
    border-bottom:3px solid var(--green);
  }
  .hanger-hole{width:44px;height:44px;border-radius:50%;background:var(--stage)}
  .welcome{
    text-align:center;font-weight:800;color:var(--green-dark);
    font-size:13px;line-height:1.15;padding:8px 6px 4px;
  }
  .hanger .welcome{font-size:11px;padding:6px 4px 3px}
  .intro{
    font-size:6.5px;line-height:1.35;color:var(--muted);
    padding:2px 10px 6px;text-align:center;
  }
  .hanger .intro{font-size:6px;padding:5px 7px 5px}
  .section-bar{
    background:var(--green);color:var(--paper);font-weight:800;
    font-size:12px;padding:3px 10px;flex:none;
  }
  .hanger .section-bar{font-size:10px;padding:2px 7px}
  .photo{flex:1;margin:6px 10px}
  .hanger .photo{margin:5px 7px}
  .photo.warm{background:linear-gradient(135deg,var(--photo-warm-a),var(--photo-warm-b))}
  .photo.cool{background:linear-gradient(135deg,var(--photo-cool-a),var(--photo-cool-b))}
  .photo-row{display:flex;gap:4px;margin:0 10px 6px;height:34px;flex:none}
  .photo-row .photo{margin:0}
  .financing{
    text-align:center;font-weight:700;font-size:10px;color:var(--green-dark);
    padding:2px 0 4px;
  }
  .hanger .financing{font-size:8.5px}
  .estimate{
    background:linear-gradient(var(--green),var(--green-dark));
    color:var(--paper);text-align:center;font-weight:800;
    font-size:11px;padding:4px 0;flex:none;
  }
  .hanger .estimate{font-size:9px;padding:3px 0}
  .footer{
    background:var(--black);color:var(--paper);
    padding:8px 6px 7px;text-align:center;flex:none;
  }
  .brand{
    display:flex;align-items:center;justify-content:center;gap:5px;
    font-weight:700;font-size:10px;letter-spacing:.5px;color:var(--paper);
  }
  .hanger .brand{font-size:8px}
  .brand-mark{width:8px;height:8px;background:var(--green)}
  .contact{font-size:5.5px;line-height:1.4;color:var(--footer-text);margin-top:3px}
</style>
</head>
<body>

  <article class="piece flyer">
    <h2 class="welcome">Windows Done Right</h2>
    <p class="intro">Quality remodeling for your home, built with care and honest pricing from start to finish.</p>
    <div class="section-bar">Windows</div>
    <div class="photo cool" role="img" aria-label="Photo of a home exterior with new windows"></div>
    <div class="photo-row">
      <div class="photo cool" role="img" aria-label="Photo of a bright window interior"></div>
      <div class="photo warm" role="img" aria-label="Photo of a window installation detail"></div>
    </div>
    <p class="financing">We offer Financing</p>
    <div class="estimate">Free Estimate</div>
    <footer class="footer">
      <div class="brand"><span class="brand-mark"></span>TALLOW RIDGE</div>
      <p class="contact">Tallow Ridge Builders, LLC · 4817 Copper Fern RD, Suite 812<br>Larkmoor, VA 00000 · Tel: 555 010 4821<br>www.tallowridgebuilders.example</p>
    </footer>
  </article>

  <article class="piece flyer">
    <h2 class="welcome">Welcome to<br>Tallow Ridge Builders</h2>
    <p class="intro">We design and build kitchens and bathrooms that fit the way you live.</p>
    <div class="section-bar">Kitchen &amp; Bathroom</div>
    <div class="photo warm" role="img" aria-label="Photo of a remodeled kitchen with wood cabinets"></div>
    <div class="photo-row">
      <div class="photo warm" role="img" aria-label="Photo of a kitchen island"></div>
      <div class="photo cool" role="img" aria-label="Photo of a remodeled bathroom"></div>
    </div>
    <p class="financing">We offer Financing</p>
    <div class="estimate">Free Estimate</div>
    <footer class="footer">
      <div class="brand"><span class="brand-mark"></span>TALLOW RIDGE</div>
      <p class="contact">Tel: 555 010 4821<br>www.tallowridgebuilders.example</p>
    </footer>
  </article>

  <article class="piece hanger">
    <div class="hanger-top"><div class="hanger-hole"></div></div>
    <p class="intro">Replacement windows that save energy and brighten every room.</p>
    <div class="section-bar">Windows</div>
    <div class="photo cool" role="img" aria-label="Photo of a home with new windows"></div>
    <p class="financing">We offer Financing</p>
    <div class="estimate">Free Estimate</div>
    <footer class="footer">
      <div class="brand"><span class="brand-mark"></span>TALLOW RIDGE</div>
      <p class="contact">555 010 4821<br>www.tallowridgebuilders.example</p>
    </footer>
  </article>

  <article class="piece hanger">
    <div class="hanger-top"><div class="hanger-hole"></div></div>
    <h2 class="welcome">Welcome to<br>Tallow Ridge</h2>
    <p class="intro">Kitchen and bath remodels done right, on time.</p>
    <div class="section-bar">Kitchen &amp; Bathroom</div>
    <div class="photo warm" role="img" aria-label="Photo of a remodeled kitchen"></div>
    <div class="estimate">Free Estimate</div>
    <footer class="footer">
      <div class="brand"><span class="brand-mark"></span>TALLOW RIDGE</div>
      <p class="contact">555 010 4821</p>
    </footer>
  </article>

</body>
</html>
```